Truck wrap Design For KV CLEANERS

Create unique and eye catching design with provide logo and information.
Also Add Cartoon or silhouette of a men with vacuum or steam cleaner.
Please Use attached template.
It must include logo that is attached. and information below:
--555-314-2097
--www.kvrapidwashpro.example
--kvrapid@wavenetmail.example
-- NFTCB MASKS TEXTILE CLEANER

Services:

Carpet, upholstery, Air duct, Dryer vent, Hard surface cleaning,

Residential/Commercial Services.

Target Market(s)

everyone

Colors

Designer to choose colors to be used in the design.

Requirements
Must have
• All the information that is provide in descricption
Should not have
• silly background.

```html
<!DOCTYPE html>
<html lang="en">
<head>
<meta charset="utf-8">
<title>KV CLEANERS – Truck Wrap Panels</title>
<link rel="stylesheet" href="https://fonts.googleapis.com/css2?family=Barlow:wght@400;500&family=Barlow+Condensed:wght@600;700&display=swap">
<style>
  :root{
    --blue:#1a73c4;
    --orange:#f7941d;
    --red-orange:#f05a28;
    --violet:#3a2f9a;
    --ink:#111111;
    --paper:#ffffff;
    --frame:#d4d4d4;
    --art:#dfe7f1;
  }
  html,body{margin:0;padding:0;width:1200px;height:1200px;overflow:hidden;background:var(--paper);}
  .wrap-sheet{display:block;width:1200px;height:1200px;}
  .panel-base{fill:var(--paper);stroke:var(--frame);stroke-width:2;}
  .band{fill:var(--blue);}
  .field{fill:var(--orange);}
  .call-box{fill:var(--paper);stroke:var(--red-orange);stroke-width:1.2;}
  .call-label{font-family:"Barlow",sans-serif;font-weight:400;fill:var(--ink);}
  .call-number{font-family:"Barlow Condensed",sans-serif;font-weight:700;fill:var(--red-orange);letter-spacing:1px;}
  .band-title{font-family:"Barlow",sans-serif;font-weight:500;fill:var(--paper);letter-spacing:1px;}
  .services-head{font-family:"Barlow Condensed",sans-serif;font-weight:700;fill:var(--violet);}
  .services-line{font-family:"Barlow Condensed",sans-serif;font-weight:600;fill:var(--violet);}
  .contact-line{font-family:"Barlow",sans-serif;font-weight:400;fill:var(--ink);}
  .brand-name{font-family:"Barlow Condensed",sans-serif;font-weight:700;fill:var(--violet);}
  .mascot-area{fill:var(--art);}
  .badge-disc{fill:var(--blue);}
  .badge-ribbon{fill:var(--orange);}
  .badge-text{font-family:"Barlow",sans-serif;font-weight:500;fill:var(--paper);}
</style>
</head>
<body>
<svg class="wrap-sheet" viewBox="0 0 1500 1500" xmlns="http://www.w3.org/2000/svg">

  <!-- Driver side box panel -->
  <g class="side-panel side-panel--left">
    <rect class="panel-base" x="322" y="72" width="555" height="345" rx="6"/>
    <polygon class="field" points="420,385 865,185 865,385"/>
    <polygon class="band" points="352,385 352,368 865,140 865,185 420,385"/>
    <g class="brand-mark">
      <text class="brand-name" x="420" y="148" font-size="22" text-anchor="middle">KV CLEANERS</text>
    </g>
    <rect class="mascot-area" x="362" y="176" width="148" height="204" rx="6" role="img" aria-label="Cartoon cleaner operating a vacuum carpet cleaner"/>
    <text class="band-title" x="690" y="252" font-size="21" text-anchor="middle" transform="rotate(-24.5 690 252)">NFTCB MASKS TEXTILE CLEANER</text>
    <rect class="call-box" x="513" y="97" width="247" height="75"/>
    <text class="call-label" x="523" y="124" font-size="24">Call Today</text>
    <text class="call-number" x="522" y="165" font-size="38">555-314-2097</text>
    <text class="services-head" x="852" y="283" font-size="38" text-anchor="end">Services:</text>
    <text class="services-line" x="852" y="311" font-size="20" text-anchor="end">Carpet, upholstery, Air duct</text>
    <text class="services-line" x="852" y="335" font-size="20" text-anchor="end">Dryer vent, Hard surface cleaning</text>
    <text class="contact-line" x="848" y="359" font-size="16" text-anchor="end">www.kvrapidwashpro.example</text>
    <text class="contact-line" x="848" y="381" font-size="16" text-anchor="end">kvrapid@wavenetmail.example</text>
  </g>

  <!-- Driver door panel with badge -->
  <g class="door-panel door-panel--left">
    <rect class="panel-base" x="185" y="280" width="132" height="180" rx="4"/>
    <g class="door-badge door-badge--small">
      <circle class="badge-disc" cx="248" cy="410" r="42"/>
      <rect class="badge-ribbon" x="194" y="398" width="110" height="22" rx="11" transform="rotate(-14 249 409)"/>
      <text class="badge-text" x="243" y="392" font-size="16" text-anchor="middle" transform="rotate(-14 243 392)">24 Hrs</text>
      <text class="badge-text" x="248" y="415" font-size="13" text-anchor="middle" transform="rotate(-14 248 415)">Emergency</text>
      <text class="badge-text" x="254" y="435" font-size="12" text-anchor="middle" transform="rotate(-14 254 435)">Service</text>
    </g>
  </g>

  <!-- Rear door panel -->
  <g class="rear-panel">
    <rect class="panel-base" x="940" y="46" width="518" height="466" rx="6"/>
    <rect class="band" x="962" y="227" width="471" height="60"/>
    <text class="band-title" x="1198" y="270" font-size="29" text-anchor="middle">NFTCB MASKS TEXTILE CLEANER</text>
    <polygon class="field" points="965,472 1350,287 1433,287 1433,472"/>
    <g class="brand-mark">
      <text class="brand-name" x="1030" y="162" font-size="24" text-anchor="middle">KV CLEANERS</text>
    </g>
    <rect class="mascot-area" x="968" y="300" width="180" height="166" rx="6" role="img" aria-label="Cartoon cleaner operating a vacuum carpet cleaner"/>
    <rect class="call-box" x="1159" y="110" width="253" height="101"/>
    <text class="call-label" x="1400" y="146" font-size="30" text-anchor="end">Call Today</text>
    <text class="call-number" x="1402" y="197" font-size="40" text-anchor="end">555-314-2097</text>
    <text class="services-head" x="1420" y="356" font-size="42" text-anchor="end">Services:</text>
    <text class="services-line" x="1422" y="392" font-size="20" text-anchor="end">Carpet, upholstery, Air duct</text>
    <text class="services-line" x="1422" y="417" font-size="20" text-anchor="end">Dryer vent, Hard surface cleaning</text>
    <text class="contact-line" x="1417" y="442" font-size="16" text-anchor="end">www.kvrapidwashpro.example</text>
    <text class="contact-line" x="1417" y="465" font-size="16" text-anchor="end">kvrapid@wavenetmail.example</text>
  </g>

  <!-- Passenger side box panel -->
  <g class="side-panel side-panel--right">
    <rect class="panel-base" x="192" y="785" width="800" height="500" rx="6"/>
    <polygon class="field" points="205,945 850,1240 205,1240"/>
    <polygon class="band" points="205,883 205,945 850,1240 947,1240 947,1215"/>
    <g class="brand-mark">
      <text class="brand-name" x="850" y="892" font-size="30" text-anchor="middle">KV CLEANERS</text>
    </g>
    <rect class="mascot-area" x="720" y="935" width="215" height="285" rx="8" role="img" aria-label="Cartoon cleaner operating a vacuum carpet cleaner"/>
    <text class="band-title" x="468" y="1042" font-size="34" text-anchor="middle" transform="rotate(24 468 1042)">NFTCB MASKS TEXTILE CLEANER</text>
    <rect class="call-box" x="357" y="822" width="355" height="108"/>
    <text class="call-label" x="372" y="860" font-size="36">Call Today</text>
    <text class="call-number" x="371" y="918" font-size="56">555-314-2097</text>
    <text class="services-head" x="222" y="1090" font-size="52">Services:</text>
    <text class="services-line" x="222" y="1131" font-size="29">Carpet, upholstery, Air duct</text>
    <text class="services-line" x="222" y="1166" font-size="29">Dryer vent, Hard surface cleaning</text>
    <text class="contact-line" x="222" y="1199" font-size="24">www.kvrapidwashpro.example</text>
    <text class="contact-line" x="222" y="1231" font-size="24">kvrapid@wavenetmail.example</text>
  </g>

  <!-- Passenger door panel with badge -->
  <g class="door-panel door-panel--right">
    <rect class="panel-base" x="998" y="1070" width="190" height="300" rx="4"/>
    <g class="door-badge door-badge--large">
      <circle class="badge-disc" cx="1088" cy="1272" r="60"/>
      <rect class="badge-ribbon" x="1016" y="1256" width="154" height="32" rx="16" transform="rotate(-14 1093 1272)"/>
      <text class="badge-text" x="1083" y="1250" font-size="24" text-anchor="middle" transform="rotate(-14 1083 1250)">24 Hrs</text>
      <text class="badge-text" x="1091" y="1281" font-size="19" text-anchor="middle" transform="rotate(-14 1091 1281)">Emergency</text>
      <text class="badge-text" x="1101" y="1309" font-size="18" text-anchor="middle" transform="rotate(-14 1101 1309)">Service</text>
    </g>
  </g>

</svg>
</body>
</html>
```